Trelva van design

I would like a striking design for this van. I have also attached photos of our other vehicles (we have a few designs, because we have a few different sections of our business pipes brite and brite plumbing), the most recent is the vac truck with the water splash running along it and we think the design works well for that particular truck . I have also attached the splash used on the vac truck and our logo. Our services are: Blocked drains, plumbing, cctv, pipe relining, Vacuum Excavation. Phone Number 48 216 385, website www.pipesbrite.example.au , Finally I thought I would attach 3 pics of vans from other companies (Swift Fitter, Flowpath Medic and Tide Rig) that I think are quite effective.
The main colours for our business are Blue, Navy, Black Grey and White
Home owners 35-65
plumbing

```html
<!DOCTYPE html>
<html lang="en">
<head>
<meta charset="utf-8">
<title>Trelva van wrap – pipes brite</title>
<link rel="stylesheet" href="https://fonts.googleapis.com/css2?family=Montserrat:wght@600&family=Roboto+Condensed:wght@700&display=swap">
<style>
  :root {
    --backdrop: #e9ecef;
    --wrap-black: #050505;
    --logo-silver: #c4c6c8;
    --accent-cyan: #1aa6d8;
    --service-white: #ffffff;
    --splash-light: #dcecf7;
    --splash-mid: #6fa8d6;
    --splash-navy: #173f8a;
    --pipe-green: #27c24a;
    --soil-brown: #3a2c22;
  }
  * { margin: 0; padding: 0; box-sizing: border-box; }
  html, body { width: 1200px; height: 539px; overflow: hidden; background: var(--backdrop); }
  .canvas { position: relative; width: 1200px; height: 539px; }
  .wrap-art { position: absolute; inset: 0; }
  .brand-name {
    position: absolute; left: 138px; top: 100px;
    font-family: "Montserrat", sans-serif; font-weight: 600;
    font-size: 72px; line-height: 72px; letter-spacing: 1px;
    color: var(--logo-silver);
  }
  .contact {
    position: absolute; left: 150px; top: 258px; width: 230px; text-align: center;
    font-family: "Roboto Condensed", sans-serif; font-weight: 700; color: var(--accent-cyan);
  }
  .contact .phone { font-size: 31px; line-height: 34px; }
  .contact .website { font-size: 22px; line-height: 28px; }
  .services {
    position: absolute; left: 484px; top: 262px; list-style: none;
    font-family: "Roboto Condensed", sans-serif; font-weight: 700;
    font-size: 19px; color: var(--service-white);
  }
  .services li { display: flex; align-items: center; gap: 10px; height: 27.5px; }
  .services svg { width: 12px; height: 18px; flex: none; }
</style>
</head>
<body>
<main class="canvas">
  <svg class="wrap-art" viewBox="0 0 1200 539" width="1200" height="539" aria-hidden="false">
    <defs>
      <linearGradient id="splashTone" x1="0" y1="0" x2="1" y2="0">
        <stop offset="0" stop-color="var(--splash-mid)"/>
        <stop offset="0.35" stop-color="var(--splash-light)"/>
        <stop offset="0.65" stop-color="var(--splash-navy)"/>
        <stop offset="1" stop-color="var(--splash-light)"/>
      </linearGradient>
      <linearGradient id="pipeTone" x1="0" y1="0" x2="1" y2="0">
        <stop offset="0" stop-color="var(--soil-brown)"/>
        <stop offset="0.4" stop-color="var(--pipe-green)"/>
        <stop offset="1" stop-color="var(--soil-brown)"/>
      </linearGradient>
    </defs>
    <path class="van-body" fill="var(--wrap-black)"
          d="M104 92 Q110 88 130 88 L760 88 Q900 92 960 140 L1080 240 Q1130 262 1140 290 L1145 440 Q1145 454 1130 454 L96 454 Q86 454 86 440 L86 120 Q88 96 104 92 Z"/>
    <rect class="pipe-photo" x="388" y="88" width="365" height="165" fill="url(#pipeTone)" opacity="0.85"
          role="img" aria-label="Photo of a green relined pipe inside an old clay drain surrounded by roots"/>
    <path class="water-splash" fill="url(#splashTone)"
          role="img" aria-label="Blue and white water splash running along the lower body"
          d="M86 300 Q140 260 200 285 Q300 320 360 335 Q420 360 470 420 Q520 440 600 430 Q700 380 780 340 Q840 310 870 270 Q940 255 1000 260 Q1050 250 1070 268 L1075 360 L1075 454 L86 454 Z"/>
  </svg>

  <h1 class="brand-name">pipes<br>brite</h1>

  <div class="contact">
    <p class="phone">48 216 385</p>
    <p class="website">pipesbrite.example.au</p>
  </div>

  <ul class="services">
    <li><svg viewBox="0 0 12 18"><path d="M6 0 C8 6 12 9 12 12.5 A6 6 0 0 1 0 12.5 C0 9 4 6 6 0 Z" fill="var(--accent-cyan)"/></svg>Blocked Drains</li>
    <li><svg viewBox="0 0 12 18"><path d="M6 0 C8 6 12 9 12 12.5 A6 6 0 0 1 0 12.5 C0 9 4 6 6 0 Z" fill="var(--accent-cyan)"/></svg>Plumbing</li>
    <li><svg viewBox="0 0 12 18"><path d="M6 0 C8 6 12 9 12 12.5 A6 6 0 0 1 0 12.5 C0 9 4 6 6 0 Z" fill="var(--accent-cyan)"/></svg>Cctv</li>
    <li><svg viewBox="0 0 12 18"><path d="M6 0 C8 6 12 9 12 12.5 A6 6 0 0 1 0 12.5 C0 9 4 6 6 0 Z" fill="var(--accent-cyan)"/></svg>Pipe Relining</li>
    <li><svg viewBox="0 0 12 18"><path d="M6 0 C8 6 12 9 12 12.5 A6 6 0 0 1 0 12.5 C0 9 4 6 6 0 Z" fill="var(--accent-cyan)"/></svg>Vacuum Excavation</li>
  </ul>
</main>
</body>
</html>
```